Business Package for Charitable Company
Lantern Drift
Business Package for Charitable Company - Fund Raising
Creative Brief
Professional
Peter Hollis
President
100 Example Way Suite 0 Portland, OR 97225
555-xxx-xxxx
555-418-xxxx
Peter@lanterndrift.example
www.lanterndrift.example
Will need to get final project files in both AI and word Formatting should include sheet of cards(on 8x11) so can go to printer Letterhead email address needs to be info@lanterndrift.example. Front of Business Card needs to have main company logo. See attached. Also on Envelop no phone numbers or email Folder put place holder for a brief description of who we are on the back side of the folder. Inside location on right hand side provide area for card. Front cover include web address and email info@lanterndrift.example only no address phone number etc. Power Point Template that has title page, bullet page and conclusion page. To be clear we need the final deliverables: FRONT AND BACK BUSINESS CARD SIZE 10 ENVELOPE AND LETTER HEAD POWER POINT PRESENTATION TEMPLATE FOLDER DESIGN WITH FLAPS FOR HOLDING PROPOSAL PAPERWORK I have uploaded from a previous project the items that I need for this project to give you a idea of what I am looking for.
Please incorporate the full tagline information: Share Freely Lift Neighbors Build Futures Want options with all Black background and white and don't include logo image (ie circle) use the file I uploaded that shows lantern standing in as the first "I" in LANTERN in the back of the card until we can take a look at things.
markpdx markpdx
Designers, Please make sure that you use my upload for example only and provide your own creative layout and design I don't need it be the same. Thanks
FONTS AND COLORS FOR LOGO ARE: Font: PerpetuaTiltingMTBold GillSansMT Color: Brown: Pantone 4485 Orange: Pantone 180 Light Orange: Pantone 718 Yellow: Pantone 116

```html
<!DOCTYPE html>
<html lang="en">
<head>
<meta charset="utf-8">
<title>Lantern Drift – Stationery Package</title>
<link href="https://fonts.googleapis.com/css2?family=Cinzel:wght@700&family=Lato:wght@400;700&display=swap" rel="stylesheet">
<style>
:root{
  --bg:#1d2f45;
  --brown:#5b2c0e;
  --brown-dark:#3a1b07;
  --orange:#f26522;
  --orange-light:#f7a35c;
  --yellow:#ffc526;
  --paper:#ffffff;
  --ink:#4a2a14;
  --rule:#d9d2cc;
}
*{margin:0;padding:0;box-sizing:border-box}
html,body{width:1200px;height:389px;overflow:hidden;background:var(--bg)}
body{position:relative;font-family:"Lato",sans-serif;color:var(--ink)}
.piece{position:absolute;overflow:hidden;background:var(--paper);box-shadow:0 1px 3px rgba(0,0,0,.45)}
.piece.dark{background:var(--brown)}
.piece.warm{background:linear-gradient(135deg,var(--yellow) 0%,var(--orange-light) 35%,var(--orange) 100%)}
.wave{position:absolute;left:0;width:100%;display:block}
.wave.bottom{bottom:0}
.wave.top{top:0}
.wordmark{font-family:"Cinzel",serif;font-weight:700;color:var(--brown);white-space:nowrap;display:flex;align-items:center;gap:.35em;letter-spacing:.03em}
.wordmark .dot{width:.9em;height:.9em;border-radius:50%;background:var(--orange);flex:none}
.wordmark.light{color:var(--paper)}
.tiny{font-size:4px;line-height:1.4;color:#7a6a60;white-space:nowrap}
.label{font-size:6px;font-weight:700;color:var(--brown);white-space:nowrap}
.slide-title{font-size:7px;font-weight:700;color:var(--brown)}
.rule{height:1px;background:var(--rule);margin:3px 0}
.tag{font-size:4px;letter-spacing:.05em;color:var(--brown);white-space:nowrap}
.cols{display:flex;font-weight:700}
.cols span{display:block}
</style>
</head>
<body>

<svg width="0" height="0" style="position:absolute" aria-hidden="true">
  <defs>
    <linearGradient id="swoosh" x1="0" y1="0" x2="1" y2="0">
      <stop offset="0" stop-color="#ffc526"/>
      <stop offset=".45" stop-color="#f7a35c"/>
      <stop offset="1" stop-color="#f26522"/>
    </linearGradient>
    <linearGradient id="swoosh-v" x1="0" y1="0" x2="0" y2="1">
      <stop offset="0" stop-color="#ffc526"/>
      <stop offset="1" stop-color="#f26522"/>
    </linearGradient>
  </defs>
</svg>

<!-- Vertical card back -->
<div class="piece dark" style="left:6px;top:6px;width:48px;height:112px">
  <svg class="wave bottom" viewBox="0 0 100 100" preserveAspectRatio="none" style="height:70%"><path d="M0 40 C40 20 60 70 100 45 L100 100 L0 100Z" fill="url(#swoosh-v)"/><path d="M0 52 C40 32 60 82 100 57" stroke="#3a1b07" stroke-width="3" fill="none"/></svg>
  <div class="wordmark light" style="position:absolute;top:14px;left:5px;font-size:5px">Lantern Drift</div>
</div>

<!-- Small cards -->
<div class="piece" style="left:62px;top:8px;width:60px;height:32px">
  <svg class="wave bottom" viewBox="0 0 100 100" preserveAspectRatio="none" style="height:45%"><path d="M0 50 C30 10 70 90 100 30 L100 100 L0 100Z" fill="url(#swoosh)"/></svg>
  <div class="wordmark" style="position:absolute;top:5px;left:5px;font-size:5px"><span class="dot"></span>Lantern Drift</div>
</div>
<div class="piece" style="left:62px;top:46px;width:60px;height:32px">
  <svg class="wave top" viewBox="0 0 100 100" preserveAspectRatio="none" style="height:35%"><path d="M0 0 L100 0 L100 50 C70 90 30 10 0 60Z" fill="url(#swoosh)"/></svg>
  <div style="position:absolute;left:5px;top:14px">
    <div class="label" style="font-size:4px">Peter Hollis</div>
    <div class="tiny">President · 555-xxx-xxxx</div>
  </div>
</div>

<!-- Wide card -->
<div class="piece" style="left:6px;top:88px;width:116px;height:46px">
  <div style="position:absolute;left:0;top:0;width:28px;height:100%;background:linear-gradient(180deg,var(--yellow),var(--orange))"></div>
  <div class="wordmark" style="position:absolute;left:34px;top:14px;font-size:9px">Lantern Drift</div>
  <div class="tag" style="position:absolute;left:34px;top:30px">Share Freely Lift Neighbors Build Futures</div>
</div>

<!-- Presentation slides -->
<div class="piece" style="left:14px;top:142px;width:104px;height:64px">
  <svg class="wave top" viewBox="0 0 100 100" preserveAspectRatio="none" style="height:22%"><path d="M0 0 L100 0 L100 60 C60 100 40 20 0 80Z" fill="url(#swoosh)"/></svg>
  <div class="slide-title" style="position:absolute;left:6px;top:18px">Our Mission</div>
  <svg style="position:absolute;left:50px;top:28px" width="48" height="28" viewBox="0 0 48 28"><rect x="2" y="14" width="6" height="14" fill="#f26522"/><rect x="12" y="8" width="6" height="20" fill="#f7a35c"/><rect x="22" y="4" width="6" height="24" fill="#5b2c0e"/><rect x="32" y="10" width="6" height="18" fill="#ffc526"/></svg>
</div>
<div class="piece" style="left:14px;top:212px;width:104px;height:64px">
  <div style="position:absolute;left:0;top:0;width:100%;height:40%;background:var(--brown)"></div>
  <div class="wordmark" style="position:absolute;left:8px;top:32px;font-size:9px">Lantern Drift</div>
  <svg class="wave bottom" viewBox="0 0 100 100" preserveAspectRatio="none" style="height:22%"><path d="M0 60 C40 0 60 100 100 30 L100 100 L0 100Z" fill="url(#swoosh)"/></svg>
</div>
<div class="piece" style="left:14px;top:282px;width:104px;height:64px">
  <svg class="wave top" viewBox="0 0 100 100" preserveAspectRatio="none" style="height:22%"><path d="M0 0 L100 0 L100 60 C60 100 40 20 0 80Z" fill="url(#swoosh)"/></svg>
  <div class="slide-title" style="position:absolute;left:6px;top:18px">Programs</div>
  <svg style="position:absolute;left:8px;top:30px" width="90" height="26" viewBox="0 0 90 26"><polyline points="0,22 15,16 30,18 45,8 60,12 75,4 90,6" fill="none" stroke="#f26522" stroke-width="2"/><line x1="0" y1="25" x2="90" y2="25" stroke="#5b2c0e"/></svg>
</div>
<div class="piece" style="left:128px;top:142px;width:104px;height:64px">
  <svg class="wave top" viewBox="0 0 100 100" preserveAspectRatio="none" style="height:22%"><path d="M0 0 L100 0 L100 60 C60 100 40 20 0 80Z" fill="url(#swoosh)"/></svg>
  <div class="slide-title" style="position:absolute;left:6px;top:18px">Key Points</div>
  <div style="position:absolute;left:8px;top:30px;width:70px"><div class="rule"></div><div class="rule"></div><div class="rule"></div><div class="rule"></div></div>
</div>
<div class="piece" style="left:128px;top:212px;width:104px;height:64px">
  <svg class="wave top" viewBox="0 0 100 100" preserveAspectRatio="none" style="height:22%"><path d="M0 0 L100 0 L100 60 C60 100 40 20 0 80Z" fill="url(#swoosh)"/></svg>
  <div class="slide-title" style="position:absolute;left:6px;top:18px">Impact</div>
  <svg style="position:absolute;left:60px;top:24px" width="34" height="34" viewBox="0 0 34 34"><circle cx="17" cy="17" r="15" fill="#f7a35c"/><path d="M17 17 L17 2 A15 15 0 0 1 31 22Z" fill="#f26522"/><path d="M17 17 L31 22 A15 15 0 0 1 8 29Z" fill="#5b2c0e"/></svg>
</div>
<div class="piece" style="left:128px;top:282px;width:104px;height:64px">
  <div style="position:absolute;inset:0;background:var(--brown)"></div>
  <div class="slide-title" style="position:absolute;left:8px;top:16px;color:#fff">Thank You</div>
  <div class="slide-title" style="position:absolute;left:8px;top:28px;color:var(--yellow);font-size:5px">Next Steps</div>
  <svg class="wave bottom" viewBox="0 0 100 100" preserveAspectRatio="none" style="height:30%"><path d="M0 60 C40 0 60 100 100 30 L100 100 L0 100Z" fill="url(#swoosh)"/></svg>
</div>

<!-- Business cards fronts & backs -->
<div class="piece" style="left:252px;top:8px;width:104px;height:56px">
  <svg class="wave bottom" viewBox="0 0 100 100" preserveAspectRatio="none" style="height:40%"><path d="M0 60 C30 10 70 100 100 30 L100 100 L0 100Z" fill="url(#swoosh)"/></svg>
  <div class="wordmark" style="position:absolute;left:8px;top:14px;font-size:7px"><span class="dot"></span>Lantern Drift</div>
</div>
<div class="piece" style="left:364px;top:8px;width:104px;height:56px">
  <svg class="wave top" viewBox="0 0 100 100" preserveAspectRatio="none" style="height:28%"><path d="M0 0 L100 0 L100 50 C70 100 30 10 0 70Z" fill="url(#swoosh)"/></svg>
  <div style="position:absolute;left:7px;top:18px">
    <div class="label">Peter Hollis</div>
    <div class="tiny">President</div>
    <div class="tiny">100 Example Way Suite 0</div>
    <div class="tiny">555-xxx-xxxx · Peter@lanterndrift.example</div>
  </div>
</div>
<div class="piece dark" style="left:252px;top:70px;width:104px;height:56px">
  <div class="wordmark light" style="position:absolute;left:10px;top:18px;font-size:7px">Lantern Drift</div>
  <div class="tag" style="position:absolute;left:10px;top:30px;color:var(--yellow)">Share Freely Lift Neighbors Build Futures</div>
</div>
<div class="piece" style="left:364px;top:70px;width:104px;height:56px">
  <svg class="wave bottom" viewBox="0 0 100 100" preserveAspectRatio="none" style="height:30%"><path d="M0 40 C40 100 60 0 100 60 L100 100 L0 100Z" fill="url(#swoosh)"/></svg>
  <div style="position:absolute;left:7px;top:8px">
    <div class="label">Peter Hollis</div>
    <div class="tiny">555-418-xxxx</div>
    <div class="tiny">www.lanterndrift.example</div>
  </div>
</div>
<div class="piece" style="left:252px;top:132px;width:104px;height:56px">
  <div style="position:absolute;right:0;top:0;width:34%;height:100%;background:linear-gradient(180deg,var(--yellow),var(--orange))"></div>
  <div class="wordmark" style="position:absolute;left:8px;top:22px;font-size:6px">Lantern Drift</div>
</div>
<div class="piece" style="left:364px;top:132px;width:104px;height:56px">
  <div style="position:absolute;left:0;top:0;width:100%;height:6px;background:var(--brown)"></div>
  <div style="position:absolute;left:7px;top:16px">
    <div class="label">Peter Hollis</div>
    <div class="tiny">Peter@lanterndrift.example</div>
  </div>
</div>

<!-- Envelopes -->
<div class="piece" style="left:492px;top:8px;width:120px;height:56px">
  <svg class="wave bottom" viewBox="0 0 100 100" preserveAspectRatio="none" style="height:40%"><path d="M0 70 C30 20 70 100 100 40 L100 100 L0 100Z" fill="url(#swoosh)"/></svg>
  <div class="wordmark" style="position:absolute;left:6px;top:6px;font-size:5px"><span class="dot"></span>Lantern Drift</div>
  <div class="tiny" style="position:absolute;left:6px;top:14px">100 Example Way Suite 0</div>
</div>
<div class="piece" style="left:622px;top:14px;width:112px;height:48px">
  <div class="wordmark" style="position:absolute;left:6px;top:6px;font-size:5px;color:var(--orange)">Lantern Drift</div>
  <div style="position:absolute;left:0;bottom:0;width:100%;height:3px;background:var(--orange)"></div>
</div>

<!-- Letterheads -->
<div class="piece" style="left:492px;top:74px;width:98px;height:150px">
  <div class="wordmark" style="position:absolute;left:6px;top:8px;font-size:6px"><span class="dot"></span>Lantern Drift</div>
  <div class="tiny" style="position:absolute;left:8px;top:30px">Dear Friend,</div>
  <div style="position:absolute;left:8px;top:38px;width:80px"><div class="rule"></div><div class="rule"></div><div class="rule"></div><div class="rule"></div><div class="rule"></div></div>
  <svg class="wave bottom" viewBox="0 0 100 100" preserveAspectRatio="none" style="height:16%"><path d="M0 50 C30 0 70 100 100 20 L100 100 L0 100Z" fill="url(#swoosh)"/></svg>
</div>
<div class="piece" style="left:600px;top:74px;width:98px;height:150px">
  <svg class="wave top" viewBox="0 0 100 100" preserveAspectRatio="none" style="height:14%"><path d="M0 0 L100 0 L100 60 C60 100 40 10 0 70Z" fill="url(#swoosh)"/></svg>
  <div class="wordmark" style="position:absolute;left:6px;top:26px;font-size:6px">Lantern Drift</div>
  <div class="tiny" style="position:absolute;left:8px;top:42px">Dear Friend,</div>
  <div style="position:absolute;left:8px;top:50px;width:80px"><div class="rule"></div><div class="rule"></div><div class="rule"></div></div>
  <div class="tiny" style="position:absolute;left:8px;bottom:6px">info@lanterndrift.example</div>
</div>
<div class="piece" style="left:708px;top:74px;width:98px;height:150px">
  <div class="wordmark" style="position:absolute;left:6px;top:8px;font-size:6px"><span class="dot"></span>Lantern Drift</div>
  <div class="tiny cols" style="position:absolute;left:8px;top:26px;width:82px"><span style="width:24px">Date</span><span style="width:32px">Item</span><span>Amount</span></div>
  <svg style="position:absolute;left:8px;top:34px" width="82" height="50" viewBox="0 0 82 50"><rect x=".5" y=".5" width="81" height="49" fill="none" stroke="#5b2c0e"/><line x1="0" y1="10" x2="82" y2="10" stroke="#5b2c0e"/><line x1="0" y1="20" x2="82" y2="20" stroke="#d9d2cc"/><line x1="0" y1="30" x2="82" y2="30" stroke="#d9d2cc"/><line x1="0" y1="40" x2="82" y2="40" stroke="#d9d2cc"/><line x1="24" y1="0" x2="24" y2="50" stroke="#5b2c0e"/><line x1="56" y1="0" x2="56" y2="50" stroke="#5b2c0e"/></svg>
  <div style="position:absolute;left:0;bottom:0;width:100%;height:4px;background:var(--orange)"></div>
</div>
<div class="piece" style="left:816px;top:74px;width:98px;height:150px">
  <div class="wordmark" style="position:absolute;left:6px;top:8px;font-size:6px"><span class="dot"></span>Lantern Drift</div>
  <div class="tiny" style="position:absolute;left:8px;top:30px">Dear Friend,</div>
  <div style="position:absolute;left:8px;top:38px;width:80px"><div class="rule"></div><div class="rule"></div><div class="rule"></div><div class="rule"></div></div>
  <div style="position:absolute;left:0;bottom:0;width:100%;height:4px;background:var(--brown)"></div>
</div>
<div class="piece" style="left:924px;top:74px;width:98px;height:150px">
  <div class="wordmark" style="position:absolute;left:6px;top:8px;font-size:6px;color:var(--orange)">Lantern Drift</div>
  <div style="position:absolute;left:8px;top:30px;width:80px"><div class="rule"></div><div class="rule"></div><div class="rule"></div><div class="rule"></div><div class="rule"></div><div class="rule"></div></div>
  <div class="tiny" style="position:absolute;left:8px;bottom:6px">www.lanterndrift.example</div>
</div>
<div class="piece" style="left:1032px;top:74px;width:98px;height:150px">
  <div class="wordmark" style="position:absolute;left:6px;top:8px;font-size:6px"><span class="dot"></span>Lantern Drift</div>
  <div class="tiny cols" style="position:absolute;left:8px;top:26px;width:82px"><span style="width:28px">Date</span><span style="width:28px">Item</span><span>Amount</span></div>
  <svg style="position:absolute;left:8px;top:34px" width="82" height="40" viewBox="0 0 82 40"><rect x=".5" y=".5" width="81" height="39" fill="none" stroke="#5b2c0e"/><line x1="0" y1="10" x2="82" y2="10" stroke="#5b2c0e"/><line x1="0" y1="20" x2="82" y2="20" stroke="#d9d2cc"/><line x1="0" y1="30" x2="82" y2="30" stroke="#d9d2cc"/><line x1="28" y1="0" x2="28" y2="40" stroke="#5b2c0e"/></svg>
</div>

<!-- Folders -->
<div class="piece warm" style="left:252px;top:200px;width:112px;height:182px">
  <div style="position:absolute;left:10px;top:14px;width:60px;height:46px;background:var(--brown)"></div>
  <div class="label" style="position:absolute;left:14px;top:20px;color:#fff">About Us</div>
  <svg class="wave bottom" viewBox="0 0 100 100" preserveAspectRatio="none" style="height:30%"><path d="M0 40 C40 0 60 80 100 20 L100 100 L0 100Z" fill="#fff"/></svg>
</div>
<div class="piece warm" style="left:370px;top:200px;width:112px;height:182px">
  <div style="position:absolute;left:0;top:0;width:100%;height:42%;background:#fff"></div>
  <div class="wordmark" style="position:absolute;left:8px;top:40px;font-size:9px">Lantern Drift</div>
  <div class="tiny" style="position:absolute;left:8px;top:168px;color:#fff">www.lanterndrift.example</div>
</div>
<div class="piece" style="left:492px;top:234px;width:206px;height:148px">
  <div style="position:absolute;left:0;top:0;width:50%;height:100%;background:linear-gradient(135deg,var(--yellow),var(--orange))"></div>
  <svg style="position:absolute;left:0;top:0;width:50%;height:100%" viewBox="0 0 100 100" preserveAspectRatio="none"><path d="M100 0 L100 100 L80 100 C100 60 60 40 90 0Z" fill="#fff"/></svg>
  <div class="wordmark" style="position:absolute;left:112px;top:56px;font-size:10px">Lantern Drift</div>
  <div class="tiny" style="position:absolute;left:112px;top:74px">info@lanterndrift.example</div>
</div>
<div class="piece" style="left:708px;top:234px;width:240px;height:148px">
  <div style="position:absolute;left:0;top:0;width:50%;height:100%;background:linear-gradient(135deg,var(--yellow),var(--orange))"></div>
  <svg style="position:absolute;left:0;top:0;width:50%;height:100%" viewBox="0 0 100 100" preserveAspectRatio="none"><path d="M100 0 L100 100 L70 100 C100 60 50 40 85 0Z" fill="#fff"/></svg>
  <div class="wordmark" style="position:absolute;left:130px;top:56px;font-size:11px">Lantern Drift</div>
  <div class="tag" style="position:absolute;left:130px;top:76px">Share Freely Lift Neighbors Build Futures</div>
</div>
<div class="piece" style="left:960px;top:238px;width:224px;height:144px">
  <div style="position:absolute;left:50%;top:0;width:1px;height:100%;background:var(--rule)"></div>
  <div style="position:absolute;left:0;bottom:0;width:100%;height:46px;background:#faf6f2;border-top:1px solid var(--rule)"></div>
  <svg class="wave bottom" viewBox="0 0 100 100" preserveAspectRatio="none" style="height:20%"><path d="M0 60 C30 10 70 100 100 30 L100 100 L0 100Z" fill="url(#swoosh)"/></svg>
  <div style="position:absolute;left:140px;top:104px;width:42px;height:22px;border:1px dashed var(--orange-light)"></div>
</div>

</body>
</html>
```